Website wordpress theme for brightwillowstudio.au

We need a modern dark mode website to entice customers to engage us to deliver web apps, mobile apps and VR apps. The site emphasises humans over tech.

Target Market(s)

Medium to large business and well funded startups

Industry/Entity Type

Information Technology

Coding

Coded - Design and coding required

Font styles to use
Sans Serif

Colors
EB3D1F
EC4F4E
F09395
F8D3D4
FCEDEE

Requirements
Must have
• Attractive image on home page

```html
<!DOCTYPE html>
<html lang="en">
<head>
<meta charset="utf-8">
<title>Bright Willow Studio</title>
<link href="https://fonts.googleapis.com/css2?family=Ubuntu:wght@400;500&family=Mukta:wght@400;500;600&display=swap" rel="stylesheet">
<style>
:root{
  --bg:#000;
  --ink:#fff;
  --ink-soft:#e6e6e6;
  --red:#a30000;
  --red-bright:#eb3d1f;
  --red-deep:#6b0000;
  --navy:#0b1020;
  --line:#777;
}
*{box-sizing:border-box;margin:0;padding:0}
html,body{width:1200px;height:3435px;overflow:hidden;background:var(--bg);color:var(--ink);font-family:"Mukta",sans-serif}
section,header,footer{position:relative;width:1200px}
.abs{position:absolute}
h1,h2,h3{font-family:"Ubuntu",sans-serif;font-weight:500}
.btn{position:absolute;display:flex;align-items:center;justify-content:center;background:#fff;color:var(--red);border-radius:30px;font-family:"Ubuntu",sans-serif;font-weight:500;font-size:18px}

/* header */
.site-header{height:87px;background:var(--bg)}
.brand{left:111px;top:22px;display:flex;align-items:center;gap:12px;font-family:"Ubuntu",sans-serif;font-size:28px;font-weight:500;color:var(--red-bright)}
.brand-dot{width:34px;height:34px;border-radius:50%;background:var(--red-bright)}
.nav{left:461px;top:32px;display:flex;gap:40px;font-size:16px}
.nav a{color:var(--ink);text-decoration:none}
.nav a.active{color:var(--red-bright)}
.header-cta{left:951px;top:17px;width:137px;height:51px}

/* hero */
.hero{height:642px;overflow:hidden}
.hero-photo{inset:0;background:
  radial-gradient(ellipse 220px 300px at 840px 330px,rgba(235,225,215,.55) 0%,rgba(200,185,170,.25) 45%,rgba(0,0,0,0) 100%),
  radial-gradient(ellipse 180px 160px at 860px 150px,rgba(90,45,25,.9) 0%,rgba(60,30,20,0) 100%),
  radial-gradient(ellipse 260px 200px at 1080px 140px,rgba(140,120,95,.6) 0%,rgba(0,0,0,0) 100%),
  radial-gradient(ellipse 200px 160px at 420px 470px,rgba(95,70,50,.7) 0%,rgba(0,0,0,0) 100%),
  radial-gradient(ellipse 300px 200px at 560px 580px,rgba(150,100,55,.55) 0%,rgba(0,0,0,0) 100%),
  linear-gradient(100deg,#0c0c0c 0%,#1e1c1a 30%,#3c342d 55%,#4a3f35 75%,#2a2420 100%)}
.hero-title{left:111px;top:159px;font-size:42px;line-height:54px;width:560px}
.hero-text{left:111px;top:278px;font-size:14px;line-height:31px;width:420px}
.hero-btn{left:111px;top:356px;width:137px;height:50px}
.hero-arrows{left:112px;top:443px;display:flex;gap:14px}
.hero-arrows span{width:28px;height:28px;border:1px solid #888;display:flex;align-items:center;justify-content:center}
.hero-arrows span.on{border-color:#fff}
.orbit{left:0;top:0}
.tag{left:776px;top:440px;width:116px;height:40px;background:#fff;color:#000;border-radius:20px;font-size:13px;font-weight:600;display:flex;align-items:center;justify-content:center}

/* how it works */
.how{height:484px}
.section-title{width:1200px;text-align:center;font-size:33px}
.section-lede{width:1200px;text-align:center;font-size:15px;line-height:31px;color:var(--ink-soft)}
.steps{left:111px;top:218px;display:flex;gap:40px}
.step{width:211px;text-align:center}
.step-label{font-size:22px;margin-top:14px}
.step-label.strong{font-weight:600}

/* about */
.about{height:560px;background:radial-gradient(ellipse at 80% 40%,#1a2b45 0%,var(--navy) 55%,#05070d 100%)}
.about-photo{left:113px;top:74px;width:454px;height:417px;background:linear-gradient(135deg,#050814 0%,#1e2a7a 45%,#7b3fc8 75%,#2a1850 100%)}
.about-title{left:599px;top:60px;font-size:33px}
.about-text{left:599px;top:116px;width:490px;font-size:15px;line-height:31px;color:var(--ink-soft)}
.about-btn{left:599px;top:440px;width:136px;height:53px}

/* services */
.services{height:734px}
.cards{left:111px;top:215px;display:flex;gap:23px}
.card{width:311px;height:435px;border:2px solid var(--red);border-radius:10px;background:linear-gradient(180deg,#0a0a0a,#140000);text-align:center;position:relative}
.card-icon{position:absolute;left:105px;top:60px;width:100px;height:100px;border-radius:50%;background:#fff;display:flex;align-items:center;justify-content:center}
.card h3{position:absolute;top:200px;width:100%;font-size:23px}
.card p{position:absolute;top:240px;left:18px;right:18px;font-size:14.5px;line-height:31px;color:var(--ink-soft)}
.card-go{position:absolute;left:143px;top:378px}

/* benefits */
.benefits{height:446px;background:radial-gradient(ellipse at 75% 50%,#1a1e33 0%,#0a0c18 60%,#05060c 100%)}
.benefits h2{left:108px;top:80px;font-size:33px}
.benefit-list{left:111px;top:135px;list-style:none;font-size:18px;line-height:40px}
.benefit-list li{display:flex;align-items:center;gap:10px}
.benefits-photo{left:727px;top:66px;width:280px;height:307px;border-radius:140px;background:linear-gradient(160deg,#4a0a10 0%,#1c2a55 50%,#6b1018 100%)}

/* footer */
.site-footer{height:482px}
.foot-title{font-size:27px;top:60px}
.quick{left:111px;top:113px;list-style:none;font-size:16px;line-height:31px}
.quick li{display:flex;align-items:center;gap:12px}
.social{left:111px;top:270px;display:flex;gap:7px}
.social span{width:31px;height:31px;border:1.5px solid #fff;border-radius:50%}
.divider{width:1px;top:87px;height:240px;border-left:1px dashed var(--line)}
.contact-item{left:368px;display:flex;gap:14px}
.contact-icon{width:35px;height:35px;border:1.5px solid #fff;border-radius:50%;display:flex;align-items:center;justify-content:center;flex:none}
.contact-item b{font-weight:500;font-size:18px;display:block;line-height:31px}
.contact-item div{font-size:16px;line-height:31px}
.rule{left:368px;width:242px;border-top:1px dashed var(--line)}
.field{left:729px;width:353px;height:40px;border:1px solid #bbb;font-size:14px;padding-left:12px;display:flex;align-items:center}
.submit{left:729px;top:260px;width:353px;height:39px;background:var(--red);font-size:16px;font-weight:600;display:flex;align-items:center;justify-content:center}
.copy-rule{left:98px;top:412px;width:1004px;border-top:1px solid #888}
.copy{top:428px;width:1200px;text-align:center;font-size:15px}
</style>
</head>
<body>

<header class="site-header">
  <div class="abs brand"><span class="brand-dot"></span>Bright Willow Studio</div>
  <nav class="abs nav">
    <a class="active" href="#">Home</a><a href="#">About Us</a><a href="#">How It Works</a><a href="#">Services</a><a href="#">Blog</a>
  </nav>
  <a class="btn header-cta">Contact Us</a>
</header>

<section class="hero">
  <div class="abs hero-photo" role="img" aria-label="Woman working on a tablet in a warmly lit evening office with a colleague at a desk behind her"></div>
  <svg class="abs orbit" width="1200" height="642" viewBox="0 0 1200 642">
    <circle cx="840" cy="310" r="222" fill="none" stroke="#fff" stroke-opacity=".35"/>
    <circle cx="840" cy="310" r="272" fill="none" stroke="#fff" stroke-opacity=".18"/>
    <circle cx="683" cy="148" r="40" fill="#fff" stroke="#ddd" stroke-width="6"/>
    <rect x="671" y="131" width="24" height="34" rx="4" fill="none" stroke="#333" stroke-width="2"/>
    <circle cx="1044" cy="320" r="40" fill="#fff" stroke="#ddd" stroke-width="6"/>
    <circle cx="1044" cy="320" r="16" fill="none" stroke="#333" stroke-width="2"/>
    <path d="M1028 320h32M1044 304v32" stroke="#333" stroke-width="2"/>
    <circle cx="744" cy="516" r="40" fill="var(--red)" stroke="#fff" stroke-width="6"/>
    <rect x="732" y="500" width="24" height="32" rx="4" fill="none" stroke="#fff" stroke-width="2"/>
    <circle cx="744" cy="516" r="7" fill="none" stroke="#fff" stroke-width="2"/>
  </svg>
  <div class="abs tag">WEB APPS</div>
  <h1 class="abs hero-title">Welcome To Bright Willow Studio</h1>
  <p class="abs hero-text">Lorem ipsum dolor sit amet, consectetur adipiscing elit, sed do eiusmod tempor incididunt ut labore et dolore magna aliqua.</p>
  <a class="btn hero-btn">Get Started</a>
  <div class="abs hero-arrows">
    <span><svg width="10" height="14"><path d="M8 1 2 7l6 6" fill="none" stroke="#999" stroke-width="2"/></svg></span>
    <span class="on"><svg width="10" height="14"><path d="M2 1l6 6-6 6" fill="none" stroke="#fff" stroke-width="2"/></svg></span>
  </div>
</section>

<section class="how">
  <h2 class="abs section-title" style="top:58px">How It Works</h2>
  <p class="abs section-lede" style="top:115px">Lorem ipsum dolor sit amet, consectetur adipiscing elit, sed do eiusmod tempor incididunt ut labore et dolore magna aliqua.<br>Ut enim ad minim veniam, quis nostrud exercitation ullamco laboris nisi ut aliquip ex ea commodo consequat.</p>
  <svg class="abs" style="left:68px;top:295px" width="14" height="20"><path d="M11 2 3 10l8 8" fill="none" stroke="#fff" stroke-width="2.5"/></svg>
  <svg class="abs" style="left:1118px;top:295px" width="14" height="20"><path d="M3 2l8 8-8 8" fill="none" stroke="#fff" stroke-width="2.5"/></svg>
  <div class="abs steps">
    <div class="step">
      <svg width="211" height="126" viewBox="0 0 211 126"><path d="M18 28a88 88 0 0 0 175 0" fill="none" stroke="var(--red-deep)" stroke-width="22" stroke-linecap="round"/><circle cx="105" cy="37" r="24" fill="none" stroke="#fff" stroke-width="3"/><path d="M129 37h18M125 24l14-8M125 50l14 8" stroke="#fff" stroke-width="2"/></svg>
      <div class="step-label">Lorem ipsum</div>
    </div>
    <div class="step">
      <svg width="211" height="126" viewBox="0 0 211 126"><path d="M18 98a88 88 0 0 1 175 0" fill="none" stroke="var(--red-deep)" stroke-width="22" stroke-linecap="round"/><rect x="76" y="62" width="22" height="16" fill="none" stroke="#fff" stroke-width="2"/><rect x="112" y="62" width="22" height="16" fill="none" stroke="#fff" stroke-width="2"/><ellipse cx="105" cy="90" rx="18" ry="10" fill="none" stroke="#fff" stroke-width="2"/><rect x="76" y="104" width="22" height="14" fill="none" stroke="#fff" stroke-width="2"/><rect x="112" y="104" width="22" height="14" fill="none" stroke="#fff" stroke-width="2"/></svg>
      <div class="step-label">Lorem ipsum</div>
    </div>
    <div class="step">
      <svg width="211" height="126" viewBox="0 0 211 126"><path d="M18 28a88 88 0 0 0 175 0" fill="none" stroke="var(--red)" stroke-width="22" stroke-linecap="round"/><circle cx="105" cy="40" r="12" fill="none" stroke="#fff" stroke-width="2.5"/><path d="M80 70h50l8 10H72z" fill="none" stroke="#fff" stroke-width="2"/><rect x="78" y="10" width="10" height="10" fill="none" stroke="#fff" stroke-width="2"/><rect x="122" y="10" width="10" height="10" fill="none" stroke="#fff" stroke-width="2"/></svg>
      <div class="step-label strong">Lorem ipsum</div>
    </div>
    <div class="step">
      <svg width="211" height="126" viewBox="0 0 211 126"><path d="M18 98a88 88 0 0 1 175 0" fill="none" stroke="var(--red-deep)" stroke-width="22" stroke-linecap="round"/><circle cx="105" cy="86" r="20" fill="none" stroke="#fff" stroke-width="2.5"/><circle cx="105" cy="86" r="8" fill="none" stroke="#fff" stroke-width="2"/><path d="M97 106v10h16v-10" fill="none" stroke="#fff" stroke-width="2"/></svg>
      <div class="step-label">Lorem ipsum</div>
    </div>
  </div>
</section>

<section class="about">
  <div class="abs about-photo" role="img" aria-label="Hand holding a glowing transparent smartphone with app icons"></div>
  <h2 class="abs about-title">About Us</h2>
  <p class="abs about-text">Lorem ipsum dolor sit amet, consectetur adipiscing elit, sed do eiusmod tempor incididunt ut labore et dolore magna aliqua. Ut enim ad minim veniam, quis nostrud exercitation ullamco laboris nisi ut aliquip ex ea commodo consequat. Duis aute irure dolor in reprehenderit in voluptate velit esse cillum dolore eu fugiat nulla pariatur. Excepteur sint occaecat cupidatat non proident, sunt in culpa qui officia deserunt mollit anim id est laborum.Sed ut perspiciatis unde omnis iste natus error sit voluptatem accusantium doloremque laudantium, totam rem aperiam, eaque ipsa quae ab illo inventore veritatis et quasi architecto beatae vitae dicta sunt explicabo.</p>
  <a class="btn about-btn">Read More</a>
</section>

<section class="services">
  <h2 class="abs section-title" style="top:62px">Our Services</h2>
  <p class="abs section-lede" style="top:115px;left:150px;width:900px">Lorem ipsum dolor sit amet, consectetur adipiscing elit, sed do eiusmod tempor incididunt ut labore et dolore magna aliqua. Ut enim ad minim veniam, quis nostrud exercitation ullamco laboris nisi ut aliquip ex ea commodo consequat.</p>
  <svg class="abs" style="left:68px;top:422px" width="18" height="18"><rect x="1" y="1" width="16" height="16" rx="4" fill="none" stroke="#aaa"/><path d="M6 9h7M10 6l3 3-3 3" fill="none" stroke="#aaa"/></svg>
  <svg class="abs" style="left:1112px;top:422px" width="18" height="18"><rect x="1" y="1" width="16" height="16" rx="4" fill="none" stroke="#fff"/><path d="M12 9H5M8 6 5 9l3 3" fill="none" stroke="#fff"/></svg>
  <div class="abs cards">
    <article class="card">
      <div class="card-icon"><svg width="50" height="50"><rect x="8" y="8" width="34" height="28" rx="3" fill="none" stroke="#333" stroke-width="2"/><circle cx="34" cy="32" r="9" fill="none" stroke="var(--red)" stroke-width="2"/></svg></div>
      <h3>Lorem ipsum dolor</h3>
      <p>Sed ut perspiciatis unde omnis iste natus doloremque laudantium, totam rem aperiam, quasi architecto beatae vitae dicta sunt explicabo.</p>
      <svg class="card-go" width="24" height="24"><circle cx="12" cy="12" r="11" fill="#fff"/><path d="M10 7l5 5-5 5" fill="none" stroke="#000" stroke-width="2.5"/></svg>
    </article>
    <article class="card">
      <div class="card-icon"><svg width="50" height="50"><circle cx="18" cy="18" r="7" fill="none" stroke="#333" stroke-width="2"/><path d="M6 38c2-8 22-8 24 0" fill="none" stroke="#333" stroke-width="2"/><rect x="28" y="8" width="14" height="24" rx="3" fill="none" stroke="var(--red)" stroke-width="2"/></svg></div>
      <h3>Lorem ipsum dolor</h3>
      <p>Sed ut perspiciatis unde omnis iste natus doloremque laudantium, totam rem aperiam, quasi architecto beatae vitae dicta sunt explicabo.</p>
      <svg class="card-go" width="24" height="24"><circle cx="12" cy="12" r="11" fill="#fff"/><path d="M10 7l5 5-5 5" fill="none" stroke="#000" stroke-width="2.5"/></svg>
    </article>
    <article class="card">
      <div class="card-icon"><svg width="50" height="50"><rect x="28" y="6" width="14" height="24" rx="3" fill="none" stroke="var(--red)" stroke-width="2"/><rect x="8" y="32" width="24" height="12" rx="3" fill="none" stroke="#333" stroke-width="2"/></svg></div>
      <h3>Lorem ipsum dolor</h3>
      <p>Sed ut perspiciatis unde omnis iste natus doloremque laudantium, totam rem aperiam, quasi architecto beatae vitae dicta sunt explicabo.</p>
      <svg class="card-go" width="24" height="24"><circle cx="12" cy="12" r="11" fill="#fff"/><path d="M10 7l5 5-5 5" fill="none" stroke="#000" stroke-width="2.5"/></svg>
    </article>
  </div>
</section>

<section class="benefits">
  <h2 class="abs">Bright Willow Studio Benefits:</h2>
  <ul class="abs benefit-list">
    <li><svg width="16" height="14"><path d="M1 7h12M8 2l5 5-5 5" fill="none" stroke="var(--red-bright)" stroke-width="3"/></svg>Lorem ipsum dolor sit amet</li>
    <li><svg width="16" height="14"><path d="M1 7h12M8 2l5 5-5 5" fill="none" stroke="var(--red-bright)" stroke-width="3"/></svg>Sed ut perspiciatis unde omnis iste natus error</li>
    <li><svg width="16" height="14"><path d="M1 7h12M8 2l5 5-5 5" fill="none" stroke="var(--red-bright)" stroke-width="3"/></svg>Lorem ipsum dolor sit amet, consectetur adipiscing</li>
    <li><svg width="16" height="14"><path d="M1 7h12M8 2l5 5-5 5" fill="none" stroke="var(--red-bright)" stroke-width="3"/></svg>Excepteur sint occaecat cupidatat non proident</li>
    <li><svg width="16" height="14"><path d="M1 7h12M8 2l5 5-5 5" fill="none" stroke="var(--red-bright)" stroke-width="3"/></svg>Sed ut perspiciatis unde omnis iste natus</li>
    <li><svg width="16" height="14"><path d="M1 7h12M8 2l5 5-5 5" fill="none" stroke="var(--red-bright)" stroke-width="3"/></svg>Quis autem vel eum iure reprehenderit qui</li>
  </ul>
  <div class="abs benefits-photo" role="img" aria-label="Hands interacting with glowing digital data interfaces"></div>
</section>

<footer class="site-footer">
  <h3 class="abs foot-title" style="left:111px">Quick Links</h3>
  <ul class="abs quick">
    <li><svg width="14" height="12"><path d="M1 6h10M7 2l4 4-4 4" fill="none" stroke="#fff" stroke-width="2.5"/></svg>Home</li>
    <li><svg width="14" height="12"><path d="M1 6h10M7 2l4 4-4 4" fill="none" stroke="#fff" stroke-width="2.5"/></svg>About Us</li>
    <li><svg width="14" height="12"><path d="M1 6h10M7 2l4 4-4 4" fill="none" stroke="#fff" stroke-width="2.5"/></svg>Services</li>
    <li><svg width="14" height="12"><path d="M1 6h10M7 2l4 4-4 4" fill="none" stroke="#fff" stroke-width="2.5"/></svg>Blog</li>
    <li><svg width="14" height="12"><path d="M1 6h10M7 2l4 4-4 4" fill="none" stroke="#fff" stroke-width="2.5"/></svg>Contact Us</li>
  </ul>
  <div class="abs social"><span></span><span></span><span></span><span></span></div>
  <div class="abs divider" style="left:315px"></div>
  <div class="abs divider" style="left:684px"></div>

  <h3 class="abs foot-title" style="left:368px">Contact Details</h3>
  <div class="abs contact-item" style="top:108px">
    <span class="contact-icon"><svg width="16" height="16"><path d="M3 2l3 0 1 4-2 1c1 2 2 3 4 4l1-2 4 1v3c-7 0-11-4-11-11z" fill="#fff"/></svg></span>
    <div><b>Phone;</b>+1 555 0142 7788</div>
  </div>
  <div class="abs rule" style="top:189px"></div>
  <div class="abs contact-item" style="top:190px">
    <span class="contact-icon"><svg width="16" height="12"><rect x="1" y="1" width="14" height="10" fill="#fff"/><path d="M1 1l7 5 7-5" fill="none" stroke="#000"/></svg></span>
    <div><b>Email:</b>info@brightwillowstudio.au</div>
  </div>
  <div class="abs rule" style="top:271px"></div>
  <div class="abs contact-item" style="top:281px">
    <span class="contact-icon"><svg width="16" height="16"><path d="M3 2l3 0 1 4-2 1c1 2 2 3 4 4l1-2 4 1v3c-7 0-11-4-11-11z" fill="#fff"/></svg></span>
    <div><b>Address:</b>Bright Willow Studio,<br>United State.</div>
  </div>

  <h3 class="abs foot-title" style="left:729px">Contact Me</h3>
  <div class="abs field" style="top:103px">Name:</div>
  <div class="abs field" style="top:156px">Email:</div>
  <div class="abs field" style="top:208px">Address:</div>
  <div class="abs submit">Submit Now</div>

  <div class="abs copy-rule"></div>
  <p class="abs copy">Copyrights@2023.Bright Willow Studio.All Rights Reserved</p>
</footer>

</body>
</html>
```